DM - management consultant

Business card - contemporary design

Front info
Dorian Maples

(Address not necessary)
PO Box 7386
Larkfield, CA 94011

(650) 555-0143
dm@dorianmapl.es

Twitter: dmq527
Facebook: /Dorian.Maples
Linkedin: /in/dorianmaples

Back or Front
www.dorianmaples.net
Facilitation & coaching, change management, strategic partnerships, business improvement

Target Market(s)

High tech businesses - mostly startups in Silicon Valley

Industry/Entity Type

Business

Font styles to use
Sans Serif

Colors

Designer to choose colors to be used in the design.

```html
<!DOCTYPE html>
<html lang="en">
<head>
<meta charset="utf-8">
<title>Dorian Maples – Business Card</title>
<link rel="stylesheet" href="https://fonts.googleapis.com/css2?family=Lato:wght@400;700;900&family=Lora:wght@700&display=swap">
<style>
  :root {
    --backdrop: #ecebe7;
    --card-white: #ffffff;
    --accent-yellow: #f3e16e;
    --name-grey: #5f5f5f;
    --ink: #1f1f1f;
    --icon-grey: #555555;
    --url-grey: #7a7a7a;
  }
  * { box-sizing: border-box; margin: 0; padding: 0; }
  html, body {
    width: 1200px;
    height: 1000px;
    overflow: hidden;
    background: var(--backdrop);
  }
  .canvas {
    position: relative;
    width: 1200px;
    height: 1000px;
  }
  .card {
    position: absolute;
    top: 350px;
    width: 520px;
    height: 300px;
    background: var(--card-white);
    box-shadow: 0 6px 18px rgba(0,0,0,0.18);
    overflow: hidden;
  }

  /* Back of card */
  .card--back { left: 60px; }
  .tagline-bubble {
    position: absolute;
    left: 26px;
    top: 50px;
    width: 468px;
    height: 136px;
    background: var(--accent-yellow);
    border-radius: 12px;
    padding: 24px 22px;
  }
  .tagline-bubble::after {
    content: "";
    position: absolute;
    left: 64px;
    bottom: -26px;
    border-top: 26px solid var(--accent-yellow);
    border-right: 30px solid transparent;
  }
  .tagline {
    font-family: "Lora", Georgia, serif;
    font-weight: 700;
    font-size: 21px;
    line-height: 1.3;
    color: var(--ink);
    white-space: nowrap;
  }
  .website {
    position: absolute;
    right: 28px;
    bottom: 40px;
    font-family: "Lato", Arial, sans-serif;
    font-size: 24px;
    font-weight: 400;
    color: var(--url-grey);
  }
  .website strong { font-weight: 900; }

  /* Front of card */
  .card--front { left: 620px; }
  .name-panel {
    position: absolute;
    left: 0; top: 0;
    width: 270px;
    height: 100%;
  }
  .name {
    position: absolute;
    left: 24px;
    bottom: 40px;
    font-family: "Lato", Arial, sans-serif;
    font-size: 38px;
    font-weight: 700;
    line-height: 1.02;
    letter-spacing: 0.5px;
    color: var(--name-grey);
  }
  .name span { display: block; }

  .info-panel {
    position: absolute;
    right: 0; top: 0;
    width: 250px;
    height: 100%;
    background: var(--accent-yellow);
    padding: 28px 10px 0 16px;
    font-family: "Lato", Arial, sans-serif;
    color: var(--ink);
  }
  .contact-list { list-style: none; }
  .contact-list li {
    display: flex;
    align-items: center;
    gap: 7px;
    font-size: 12px;
    font-weight: 700;
    line-height: 1.6;
    white-space: nowrap;
  }
  .contact-list svg { width: 12px; height: 12px; flex: none; fill: var(--icon-grey); }

  .social-list { list-style: none; margin-top: 28px; }
  .social-list li {
    display: flex;
    align-items: center;
    gap: 12px;
    margin-bottom: 12px;
    font-size: 14px;
    font-weight: 700;
    line-height: 1.1;
  }
  .social-dot {
    width: 32px; height: 32px;
    border-radius: 50%;
    background: var(--ink);
    flex: none;
  }
</style>
</head>
<body>
<main class="canvas">

  <section class="card card--back" aria-label="Business card back">
    <div class="tagline-bubble">
      <p class="tagline">Facilitation &amp; coaching, change<br>Management, strategic partnerships,<br>Business improvement</p>
    </div>
    <p class="website">www.dorian<strong>maples</strong>.net</p>
  </section>

  <section class="card card--front" aria-label="Business card front">
    <div class="name-panel">
      <h1 class="name">
        <span>DORIAN</span>
        <span>MAPLES</span>
      </h1>
    </div>
    <div class="info-panel">
      <ul class="contact-list">
        <li>
          <svg viewBox="0 0 24 24" aria-hidden="true"><path d="M12 2a7 7 0 0 0-7 7c0 5 7 13 7 13s7-8 7-13a7 7 0 0 0-7-7zm0 9.5A2.5 2.5 0 1 1 12 6.5a2.5 2.5 0 0 1 0 5z"/></svg>
          PO Box 7386, Larkfield, CA 94011
        </li>
        <li>
          <svg viewBox="0 0 24 24" aria-hidden="true"><path d="M7 1h10a2 2 0 0 1 2 2v18a2 2 0 0 1-2 2H7a2 2 0 0 1-2-2V3a2 2 0 0 1 2-2zm0 3v14h10V4H7zm5 15.5a1 1 0 1 0 0 2 1 1 0 0 0 0-2z"/></svg>
          (650) 555-0143
        </li>
        <li>
          <svg viewBox="0 0 24 24" aria-hidden="true"><path d="M2 5h20v14H2V5zm2 2v.5l8 5 8-5V7H4zm0 2.9V17h16V9.9l-8 5-8-5z"/></svg>
          dm@dorianmapl.es
        </li>
      </ul>
      <ul class="social-list">
        <li><span class="social-dot"></span><span>friendspace.com/<br>Dorian.Maples</span></li>
        <li><span class="social-dot"></span><span>workroster.com/<br>in/dorianmaples</span></li>
        <li><span class="social-dot"></span><span>shortpost.com/<br>dmq527</span></li>
      </ul>
    </div>
  </section>

</main>
</body>
</html>
```